Business card design Needed for new logo / Construction business, home extensions and new builds

We need a business card design using our new logo files which i will attach to this project :)

We are a small construction business specialising in home extensions, new builds and property development. We are very ambitious and would appreciate professional and elegant designs for our new business card.

Very serious about using the services on Sketchwharf and recently acquired our new logo from here :)

Please get involved, i will feedback when i can as i am very busy but can respond daily, thanks

Target Market(s)

People that want to build onto their houses, new building developments or adding too their existing property

Industry/Entity Type

Construction

Contact Information for Business Card

Thornley Pike Construction, Wilbur Fenwick (Managing Director), Tel 07829456172, email - info@thornley-pike, www.thornley-pike.co.uk

Colors

Designer to choose colors to be used in the design.

Requirements
Must have
• I like a deep grey on the back please. A lot of you have provided black from and back, try mixing things up a little. The black looks cool 😎 Thanks

```html
<!DOCTYPE html>
<html lang="en">
<head>
<meta charset="utf-8">
<title>Thornley Pike Construction – Business Card</title>
<link rel="stylesheet" href="https://fonts.googleapis.com/css2?family=Cinzel:wght@500&family=Roboto+Slab:wght@700&family=Libre+Baskerville&display=swap">
<style>
  :root {
    --backdrop: #d6d6d6;
    --ink: #111111;
    --panel-black: #070707;
    --deep-grey-1: #2c2c2c;
    --deep-grey-2: #141414;
    --silver-1: #e9eaeb;
    --silver-2: #aeb0b3;
    --silver-3: #d7d8da;
    --gold-1: #c99528;
    --gold-2: #f0c979;
    --gold-3: #b98322;
    --edge-grey: #6d6e70;
    --brand-silver: #d4d5d7;
  }
  * { margin: 0; padding: 0; box-sizing: border-box; }
  html, body { width: 1200px; height: 900px; overflow: hidden; }
  body {
    background: var(--backdrop);
    display: flex;
    flex-direction: column;
    align-items: center;
    justify-content: center;
    gap: 40px;
  }
  .card {
    position: relative;
    width: 700px;
    height: 400px;
    overflow: hidden;
    box-shadow: 0 10px 24px rgba(0,0,0,0.25);
  }
  .card-art { position: absolute; inset: 0; width: 100%; height: 100%; }

  /* back side */
  .card-back-pattern {
    position: absolute; inset: 0;
    background: radial-gradient(ellipse at 55% 40%, var(--deep-grey-1), var(--deep-grey-2) 75%);
  }
  .back-brand {
    position: absolute;
    right: 44px;
    top: 178px;
    display: flex;
    align-items: center;
    gap: 8px;
    font-family: "Cinzel", serif;
    font-weight: 500;
    font-size: 13px;
    letter-spacing: 1px;
    color: var(--gold-1);
  }
  .brand-square { width: 12px; height: 12px; background: var(--gold-1); }

  /* front side */
  .holder {
    position: absolute;
    left: 52px;
    top: 92px;
    color: var(--ink);
  }
  .holder-name {
    font-family: "Roboto Slab", serif;
    font-weight: 700;
    font-size: 22px;
    letter-spacing: 0.5px;
  }
  .holder-role {
    font-family: "Libre Baskerville", serif;
    font-size: 16px;
    color: #2b2b2b;
    margin-top: 2px;
  }
  .contacts {
    position: absolute;
    left: 52px;
    bottom: 36px;
    list-style: none;
    font-family: "Libre Baskerville", serif;
    font-size: 17px;
    color: var(--ink);
  }
  .contacts li { display: flex; align-items: center; gap: 10px; line-height: 32px; }
  .contacts svg { width: 16px; height: 16px; flex: none; }
  .front-brand {
    position: absolute;
    left: 400px;
    top: 150px;
    width: 270px;
    display: flex;
    flex-direction: column;
    align-items: center;
    gap: 14px;
    font-family: "Cinzel", serif;
    font-weight: 500;
    font-size: 24px;
    line-height: 1.25;
    letter-spacing: 1.5px;
    text-align: center;
    color: var(--brand-silver);
  }
  .front-brand .brand-square { width: 22px; height: 22px; background: var(--brand-silver); }
</style>
</head>
<body>

  <section class="card card-back" aria-label="Card back">
    <div class="card-back-pattern" role="img" aria-label="Deep grey background with an embossed repeating brand pattern"></div>
    <div class="back-brand"><span class="brand-square"></span>Thornley Pike</div>
  </section>

  <section class="card card-front" aria-label="Card front">
    <svg class="card-art" viewBox="0 0 700 400" preserveAspectRatio="none" aria-hidden="true">
      <defs>
        <linearGradient id="silverBand" x1="0" y1="0" x2="1" y2="0.3">
          <stop offset="0" stop-color="var(--silver-2)"/>
          <stop offset="0.45" stop-color="var(--silver-1)"/>
          <stop offset="0.7" stop-color="var(--silver-2)"/>
          <stop offset="1" stop-color="var(--silver-3)"/>
        </linearGradient>
        <linearGradient id="goldBand" x1="0" y1="0" x2="1" y2="0">
          <stop offset="0" stop-color="var(--gold-1)"/>
          <stop offset="0.45" stop-color="var(--gold-2)"/>
          <stop offset="1" stop-color="var(--gold-3)"/>
        </linearGradient>
      </defs>
      <rect class="silver-band" width="700" height="400" fill="url(#silverBand)"/>
      <polygon class="gold-band" points="0,190 280,180 570,400 0,400" fill="url(#goldBand)"/>
      <polygon class="edge-stripe" points="620,0 700,0 700,400 560,400 262,186" fill="var(--edge-grey)"/>
      <polygon class="black-panel" points="640,0 700,0 700,400 580,400 290,188" fill="var(--panel-black)"/>
    </svg>

    <div class="holder">
      <p class="holder-name">WILBUR FENWICK</p>
      <p class="holder-role">Managing Director</p>
    </div>

    <ul class="contacts">
      <li>
        <svg viewBox="0 0 16 16"><path d="M3 2h3l1 3-2 1.5a9 9 0 0 0 4.5 4.5L11 9l3 1v3a1 1 0 0 1-1 1A12 12 0 0 1 2 3a1 1 0 0 1 1-1z" fill="var(--ink)"/></svg>
        07829456172
      </li>
      <li>
        <svg viewBox="0 0 16 16"><rect x="1" y="3" width="14" height="10" rx="1" fill="var(--ink)"/><path d="M1.5 3.5 8 9l6.5-5.5" stroke="var(--gold-2)" stroke-width="1.3" fill="none"/></svg>
        info@thornley-pike.co.uk
      </li>
      <li>
        <svg viewBox="0 0 16 16"><circle cx="8" cy="8" r="6.2" fill="none" stroke="var(--ink)" stroke-width="1.6"/><path d="M2 8h12M8 2c-3 3.5-3 8.5 0 12M8 2c3 3.5 3 8.5 0 12" stroke="var(--ink)" stroke-width="1.1" fill="none"/></svg>
        www.thornley-pike.co.uk
      </li>
    </ul>

    <div class="front-brand">
      <span class="brand-square"></span>
      <p>Thornley Pike<br>Construction</p>
    </div>
  </section>

</body>
</html>
```